Brightmere Business Card Redesign & Logo Update

We need to update our business cards to something more modern and fresh. Brightmere can provide the current color schemes and old design examples, but welcome creativity in helping us with this redesign. PLEASE NOTE that we no longer utilize the "tree" and/or "leaf" imagery in our branding. If able would apprecaite an update on the quality of our "words only" logo in Ai. / PNG formats too.

Target Market(s)

Investors, landowners, corporate partners, contractors

Industry/Entity Type

Environmental Restoration & Conservation

Contact Information for Business Card

Logo, persons name, title, mailing address, phone and email, website url

Font styles to use
Other font styles liked:
• Merriweather

Requirements
Nice to have
• Logo, persons name, title, mailing address, phone and email, website url, but open to ideams
Should not have
• No all back backgrounds

```html
<!DOCTYPE html>
<html lang="en">
<head>
<meta charset="utf-8">
<title>Brightmere Business Card</title>
<link rel="stylesheet" href="https://fonts.googleapis.com/css2?family=Oswald:wght@500;700&family=Poppins:wght@400;500&display=swap">
<style>
  :root {
    --canvas: #e6e7e6;
    --green: #1b8441;
    --green-dark: #137a3a;
    --orange: #ee7d22;
    --ink: #151515;
    --paper: #ffffff;
    --rule: #c9c9c9;
  }
  * { box-sizing: border-box; margin: 0; padding: 0; }
  html, body { width: 1200px; height: 880px; overflow: hidden; }
  body {
    background: var(--canvas);
    display: flex;
    flex-direction: column;
    align-items: center;
    justify-content: center;
    gap: 40px;
  }
  .card {
    width: 700px;
    height: 400px;
    border-radius: 22px;
    position: relative;
    overflow: hidden;
    box-shadow: 0 6px 18px rgba(0,0,0,0.12);
  }

  /* Front */
  .card-front {
    background: linear-gradient(135deg, #2a9a57 0%, var(--green) 45%, var(--green-dark) 100%);
    display: flex;
    flex-direction: column;
    align-items: center;
    justify-content: center;
  }
  .front-wordmark {
    font-family: "Oswald", sans-serif;
    font-weight: 700;
    font-size: 96px;
    letter-spacing: 1px;
    color: var(--ink);
    text-transform: uppercase;
    line-height: 1;
  }
  .front-url {
    position: absolute;
    bottom: 58px;
    left: 0; right: 0;
    text-align: center;
    font-family: "Oswald", sans-serif;
    font-weight: 500;
    font-size: 15px;
    letter-spacing: 1.5px;
    color: var(--ink);
    text-transform: uppercase;
  }

  /* Back */
  .card-back {
    background: var(--paper);
    display: grid;
    grid-template-columns: 395px 1px 1fr;
    align-items: center;
  }
  .back-brand {
    display: flex;
    justify-content: center;
    align-items: center;
    padding-top: 70px;
  }
  .back-wordmark {
    font-family: "Oswald", sans-serif;
    font-weight: 700;
    font-size: 64px;
    color: var(--green);
    text-transform: uppercase;
    line-height: 1;
  }
  .divider {
    width: 1px;
    height: 230px;
    background: var(--rule);
  }
  .contact {
    padding-left: 26px;
    font-family: "Poppins", sans-serif;
    color: var(--ink);
  }
  .person-name {
    font-family: "Oswald", sans-serif;
    font-weight: 500;
    font-size: 34px;
    line-height: 1;
    text-transform: uppercase;
  }
  .person-name .first { color: var(--orange); }
  .person-name .last { color: var(--green); }
  .person-title {
    font-family: "Oswald", sans-serif;
    font-weight: 700;
    font-size: 18px;
    text-transform: uppercase;
    margin-top: 4px;
    margin-bottom: 14px;
  }
  .contact-list { list-style: none; }
  .contact-list li {
    display: flex;
    align-items: center;
    gap: 10px;
    font-size: 14px;
    line-height: 24px;
  }
  .contact-list svg { width: 14px; height: 14px; flex: none; }
  .address {
    margin-top: 12px;
    padding-left: 24px;
    font-size: 14px;
    line-height: 22px;
    font-style: normal;
  }
</style>
</head>
<body>

  <section class="card card-front" aria-label="Business card front">
    <div class="front-wordmark">Brightmere</div>
    <div class="front-url">www.brightmereecc.com</div>
  </section>

  <section class="card card-back" aria-label="Business card back">
    <div class="back-brand">
      <div class="back-wordmark">Brightmere</div>
    </div>
    <div class="divider"></div>
    <div class="contact">
      <div class="person-name"><span class="first">Dana</span> <span class="last">Reyes</span></div>
      <div class="person-title">Managing Director</div>
      <ul class="contact-list">
        <li>
          <svg viewBox="0 0 24 24" aria-hidden="true"><path fill="#ee7d22" d="M6.6 10.8a15.1 15.1 0 0 0 6.6 6.6l2.2-2.2a1 1 0 0 1 1-.25 11.4 11.4 0 0 0 3.6.57 1 1 0 0 1 1 1V20a1 1 0 0 1-1 1A17 17 0 0 1 3 4a1 1 0 0 1 1-1h3.5a1 1 0 0 1 1 1c0 1.25.2 2.45.57 3.57a1 1 0 0 1-.25 1z"/></svg>
          555-014-2738
        </li>
        <li>
          <svg viewBox="0 0 24 24" aria-hidden="true"><rect x="2" y="5" width="20" height="14" rx="2" fill="#ee7d22"/><path d="M3 6l9 7 9-7" fill="none" stroke="#fff" stroke-width="1.8"/></svg>
          dana@brightmeremail.com
        </li>
        <li>
          <svg viewBox="0 0 24 24" aria-hidden="true"><g fill="none" stroke="#ee7d22" stroke-width="2"><circle cx="12" cy="12" r="9"/><ellipse cx="12" cy="12" rx="4" ry="9"/><path d="M3 12h18"/></g></svg>
          www.brightmereecc.com
        </li>
      </ul>
      <address class="address">
        118 Alder Crest Road<br>
        Suite 210, Fernvale<br>
        OR 97031
      </address>
    </div>
  </section>

</body>
</html>
```